2018 PVLTA Conference Theme Artwork

We need artwork designed around the theme of this year's human resources conference. The theme is "Celebrating 20 Years Together Towards Tomorrow". The artwork should be designed as a 4x6 postcard and will eventually be adapted/reformatted to use on the registration website, sales materials, e-newsletters, conference guide cover and signage.

Target Market(s)

Attendees are human resources professionals. Exhibitors and sponsors are companies who want to sell their products/services to human resource professionals

Colors

Designer to choose colors to be used in the design.

Requirements
Must have
• NO BORING PIXVAULT IMAGERY PLEASE.
• Theme: Celebrating 20 Years Together Towards Tomorrow
• Event: 20th Annual PVLT Conference
• Dates/Times: Tuesday, May 15, 2018, 12:30pm - 5:00pm and Wednesday, May 16, 2018 7:30am - 5:30pm
• Website: pvltsummit.example
• Location: The HALL at the Corvane Lindley
Nice to have
• Engaging, celebratory, visually attractive
Should not have
• NO BORING PIXVAULT IMAGERY.

```html
<!DOCTYPE html>
<html lang="en">
<head>
<meta charset="utf-8">
<title>20th Annual PVLT Conference – Celebrating 20 Years</title>
<link rel="stylesheet" href="https://fonts.googleapis.com/css2?family=Archivo+Black&family=Barlow:wght@500;600&display=swap">
<style>
  :root {
    --sky: #5fb5e6;
    --sky-light: #a8dcf7;
    --sky-deep: #4aa6dc;
    --navy: #0b4a7c;
    --white: #ffffff;
    --numeral-side: #cfd6dc;
  }
  * { margin: 0; padding: 0; box-sizing: border-box; }
  html, body { width: 1200px; height: 800px; overflow: hidden; }
  body {
    font-family: "Barlow", Arial, sans-serif;
    background: radial-gradient(ellipse 70% 75% at 35% 55%, var(--sky-light) 0%, var(--sky) 55%, var(--sky-deep) 100%);
  }
  .postcard { position: relative; width: 1200px; height: 800px; }
  .crowd-art {
    position: absolute;
    left: 40px; top: 200px;
    width: 640px; height: 545px;
    border-radius: 50%;
    background: radial-gradient(circle at 50% 40%, rgba(255,255,255,0.45) 0%, rgba(255,255,255,0.15) 45%, rgba(255,255,255,0) 72%);
  }
  .headline { position: absolute; left: 0; top: 0; }
  .headline text { font-family: "Archivo Black", "Arial Black", sans-serif; }
  .headline .celebrating { fill: var(--white); filter: drop-shadow(0 4px 6px rgba(0,40,80,0.25)); }
  .headline .anniversary { fill: var(--white); filter: drop-shadow(10px 8px 0 var(--numeral-side)); }
  .headline .years { fill: var(--white); }
  .headline .theme { fill: var(--navy); }
  .event-details {
    position: absolute;
    right: 64px; top: 548px;
    text-align: right;
  }
  .event-title {
    color: var(--white);
    font-weight: 600;
    font-size: 32px;
    line-height: 1;
    margin-bottom: 27px;
  }
  .event-title sup { font-size: 18px; vertical-align: 12px; }
  .event-info {
    color: var(--navy);
    font-weight: 500;
    font-size: 24px;
    line-height: 30px;
  }
  .event-site {
    color: var(--white);
    font-weight: 600;
    font-size: 29px;
    line-height: 1;
    margin-top: 31px;
  }
</style>
</head>
<body>
<main class="postcard">
  <div class="crowd-art" role="img" aria-label="Illustration of a crowd of small people gathering around the large number 20 bursting with confetti"></div>

  <svg class="headline" width="1200" height="800" viewBox="0 0 1200 800" aria-label="Celebrating 20 Years Together Towards Tomorrow">
    <text class="celebrating" x="60" y="176" font-size="168" textLength="1080" lengthAdjust="spacingAndGlyphs">CELEBRATING</text>
    <text class="anniversary" x="352" y="476" font-size="340" textLength="266" lengthAdjust="spacingAndGlyphs">20</text>
    <g class="years" font-size="44" text-anchor="middle">
      <text x="672" y="262">Y</text>
      <text x="672" y="318">E</text>
      <text x="672" y="374">A</text>
      <text x="672" y="430">R</text>
      <text x="672" y="490">S</text>
    </g>
    <text class="theme" x="720" y="296" font-size="94" textLength="416" lengthAdjust="spacingAndGlyphs">TOGETHER</text>
    <text class="theme" x="720" y="398" font-size="94" textLength="416" lengthAdjust="spacingAndGlyphs">TOWARDS</text>
    <text class="theme" x="720" y="494" font-size="94" textLength="416" lengthAdjust="spacingAndGlyphs">TOMORROW</text>
  </svg>

  <section class="event-details">
    <h1 class="event-title">20<sup>th</sup> Annual PVLT Conference</h1>
    <p class="event-info">Tuesday, May 15, 2018 | 12:30pm-5:00pm</p>
    <p class="event-info">Wednesday, May 16, 2018 | 7:30am-5:30pm</p>
    <p class="event-info">The HALL at the Corvane Lindley</p>
    <p class="event-site">pvltsummit.example</p>
  </section>
</main>
</body>
</html>
```